PowerPoint Design Project

I need a Power Point slide template designed with 4 or 5 slides. We are a health care technology company and would like to take our current look and feel in this PP presentation to the next level and "prettied up"

Target Market(s)

Health Care Professionals

Industry/Entity Type

Health

Requirements
Must have
• Cannot change out the TOLVARE logo. The logo is all CAPS
Should not have
• The color blue is restricted and cannot be used.

```html
<!DOCTYPE html>
<html lang="en">
<head>
<meta charset="UTF-8">
<title>Tolvare – Welcome</title>
<link rel="stylesheet" href="https://fonts.googleapis.com/css2?family=Arimo:wght@400;700&display=swap">
<style>
  :root {
    --brand-green: #b1bf37;
    --brand-gray: #939598;
    --text-gray: #8a8c8f;
    --paper: #ffffff;
    --ink-light: #ffffff;
  }
  * { margin: 0; padding: 0; box-sizing: border-box; }
  html, body {
    width: 1200px;
    height: 900px;
    overflow: hidden;
    background: var(--paper);
  }
  .slide {
    position: relative;
    width: 1200px;
    height: 900px;
    background: var(--paper);
    font-family: "Arimo", Arial, sans-serif;
    overflow: hidden;
  }
  .brand {
    position: absolute;
    left: 60px;
    top: 170px;
    display: flex;
    align-items: center;
    gap: 40px;
  }
  .brand-square {
    width: 50px;
    height: 50px;
    background: var(--brand-green);
  }
  .brand-name {
    font-size: 58px;
    font-weight: 700;
    letter-spacing: 5px;
    color: var(--brand-gray);
    line-height: 1;
  }
  .title-band {
    position: absolute;
    left: 0;
    top: 397px;
    width: 867px;
    height: 266px;
    background: var(--brand-green);
    color: var(--ink-light);
    padding: 38px 0 0 60px;
  }
  .title-band h1 {
    font-size: 80px;
    font-weight: 700;
    letter-spacing: -1px;
    line-height: 1.1;
  }
  .title-band p {
    margin-top: 26px;
    font-size: 17px;
    letter-spacing: -0.3px;
  }
  .footer {
    position: absolute;
    left: 33px;
    top: 838px;
    display: flex;
    align-items: center;
    gap: 12px;
    font-size: 13px;
  }
  .page-number {
    width: 34px;
    height: 34px;
    border-radius: 50%;
    background: var(--brand-green);
    color: var(--ink-light);
    font-weight: 700;
    font-size: 13px;
    display: flex;
    align-items: center;
    justify-content: center;
  }
  .footer-company { color: var(--brand-green); font-weight: 700; }
  .footer-note { color: var(--text-gray); }
</style>
</head>
<body>
  <main class="slide">
    <header class="brand">
      <div class="brand-square"></div>
      <span class="brand-name">TOLVARE</span>
    </header>

    <section class="title-band">
      <h1>Welcome</h1>
      <p>Lorem ipsum dolor sit amet, consectetuer adipiscing elit. Aenean commodo ligula eget dolor.</p>
    </section>

    <footer class="footer">
      <span class="page-number">1</span>
      <span class="footer-company">TOLVARE Network Inc</span>
      <span class="footer-note">|&nbsp; Company Confidential</span>
    </footer>
  </main>
</body>
</html>
```